Silver Arch Consulting Website Design

I already have a live website. Just want some help with design, finishing up the project. I also have another site with wix that I am ready to have designed. I am not completely sure on the pages but will for sure need "coaching", "training", "resources". Most of the people I currently work with are real estate brokers and mortgage brokers but I want to be able to appeal to all industries.
Number of Pages Required
4 page
Font styles to use
Sans Serif
Colors
Requirements
Must have
- place holders for video
Nice to have
- a way for people to purchase digital downloads

```html
<!DOCTYPE html>
<html lang="en">
<head>
<meta charset="UTF-8">
<title>Silver Arch Consulting — Blog &amp; Contact</title>
<link href="https://fonts.googleapis.com/css2?family=Montserrat:wght@200;300;400;900&family=Poppins:wght@400;600&display=swap" rel="stylesheet">
<style>
  :root {
    --page-bg: #eff0ef;
    --dark: #3f3e44;
    --dark-deep: #35343a;
    --news-ghost: #4a494f;
    --red: #e8322a;
    --white: #ffffff;
    --ink: #2b2b2e;
    --muted: #b9b9bc;
    --field-line: #d6d6d8;
    --map: #e4e4e4;
    --brand: #5a1c1c;
  }
  * { margin: 0; padding: 0; box-sizing: border-box; }
  html, body { width: 960px; height: 1200px; overflow: hidden; }
  body {
    background: var(--page-bg);
    font-family: "Montserrat", sans-serif;
    position: relative;
  }
  .site { position: absolute; left: 70px; top: 0; width: 820px; }

  /* Blog */
  .blog { position: relative; height: 417px; background: var(--dark); overflow: hidden; }
  .blog-ghost {
    position: absolute; left: 82px; top: 30px;
    font-weight: 900; font-size: 96px; letter-spacing: -2px;
    color: var(--news-ghost); line-height: 1;
  }
  .blog-title {
    position: absolute; left: 84px; top: 100px;
    font-weight: 300; font-size: 30px; color: var(--white);
  }
  .blog-title span, .contact-title span { color: var(--red); }
  .blog-rule { position: absolute; left: 0; top: 143px; width: 208px; height: 2px; background: var(--red); }

  .card { position: absolute; top: 170px; width: 205px; height: 196px; overflow: hidden; }
  .card-1 { left: 88px; } .card-2 { left: 306px; } .card-3 { left: 524px; }
  .card-photo { position: absolute; inset: 0; background: linear-gradient(160deg, #f1f3f5 0%, #d7dde3 55%, #b9a893 100%); }
  .card-3 .card-photo { background: linear-gradient(160deg, #eef1f4 0%, #cfd6dd 50%, #7d7f86 100%); }
  .card-tag {
    position: absolute; left: 27px; top: 24px; width: 62px; height: 19px;
    border-radius: 10px; background: var(--red); color: #ffb8b3;
    font-size: 7px; line-height: 19px; text-align: center; letter-spacing: .3px;
  }
  .card-meta { position: absolute; left: 27px; top: 134px; font-family: "Poppins", sans-serif; font-size: 6px; color: #555; }
  .card-heading {
    position: absolute; left: 27px; top: 144px; width: 160px;
    font-family: "Poppins", sans-serif; font-weight: 600; font-size: 10px; line-height: 16px; color: #3a3a3c;
  }

  /* Contact */
  .contact { position: relative; height: 391px; background: var(--white); }
  .contact-title {
    position: absolute; left: 84px; top: 58px;
    font-weight: 300; font-size: 30px; color: var(--ink);
  }
  .contact-rule { position: absolute; left: 0; top: 104px; width: 355px; height: 2px; background: var(--red); }
  .field { position: absolute; left: 88px; width: 221px; border-bottom: 1px solid var(--field-line); font-size: 10px; color: #c8c8ca; font-weight: 300; }
  .field-name { top: 161px; height: 15px; }
  .field-email { top: 202px; height: 15px; }
  .field-message { top: 244px; height: 60px; }
  .send {
    position: absolute; left: 86px; top: 332px; width: 99px; height: 27px;
    border-radius: 14px; background: var(--red); color: var(--white);
    font-size: 14px; text-align: center; line-height: 27px;
  }
  .map { position: absolute; left: 408px; top: 0; width: 412px; height: 391px; background: var(--map); }

  /* Footer */
  .footer { position: relative; height: 165px; background: var(--dark); }
  .brand { position: absolute; left: 87px; top: 45px; width: 80px; font-weight: 400; font-size: 12px; line-height: 14px; color: var(--brand); }
  .social { position: absolute; left: 92px; top: 101px; display: flex; gap: 16px; }
  .social span { width: 9px; height: 9px; border-radius: 50%; background: #8a8a8f; }
  .footer-heading { position: absolute; top: 51px; font-weight: 300; font-size: 14px; color: var(--red); }
  .links-heading { left: 291px; } .news-heading { left: 484px; }
  .links { position: absolute; left: 293px; top: 75px; list-style: none; font-size: 10px; line-height: 12.5px; color: #c4c4c7; font-weight: 300; }
  .signup { position: absolute; left: 484px; top: 85px; width: 212px; height: 30px; border-radius: 15px; background: var(--dark-deep); }
  .signup-input { position: absolute; left: 16px; top: 0; font-size: 10px; line-height: 30px; color: #77767c; font-weight: 300; }
  .signup-btn { position: absolute; right: 0; top: 0; width: 82px; height: 30px; border-radius: 15px; background: var(--red); color: var(--white); font-size: 13px; text-align: center; line-height: 30px; }
</style>
</head>
<body>
<div class="site">
  <section class="blog">
    <div class="blog-ghost">NEWS</div>
    <h2 class="blog-title">Our <span>Blog</span></h2>
    <div class="blog-rule"></div>

    <article class="card card-1">
      <div class="card-photo" role="img" aria-label="Photo of two colleagues talking in a bright office"></div>
      <div class="card-tag">BUSINESS</div>
      <div class="card-meta">ADMIN &nbsp; MAY 3, 2018</div>
      <h3 class="card-heading">Software Defined Networking in Business Security</h3>
    </article>
    <article class="card card-2">
      <div class="card-photo" role="img" aria-label="Photo of a man working at a desk with a laptop"></div>
      <div class="card-tag">BUSINESS</div>
      <div class="card-meta">ADMIN &nbsp; MAY 3, 2018</div>
      <h3 class="card-heading">The Uncharted Channel in Marketing Research</h3>
    </article>
    <article class="card card-3">
      <div class="card-photo" role="img" aria-label="Photo of a businessman in a suit adjusting his tie"></div>
      <div class="card-tag">BUSINESS</div>
      <div class="card-meta">ADMIN &nbsp; MAY 3, 2018</div>
      <h3 class="card-heading">Transform the Customer Experience Wisely</h3>
    </article>
  </section>

  <section class="contact">
    <h2 class="contact-title">Let’s Work <span>Together</span></h2>
    <div class="contact-rule"></div>
    <div class="field field-name">Name</div>
    <div class="field field-email">Email</div>
    <div class="field field-message">Message</div>
    <div class="send">send</div>
    <div class="map" role="img" aria-label="Street map showing the office location"></div>
  </section>

  <footer class="footer">
    <div class="brand">Silver Arch Consulting</div>
    <div class="social" aria-label="Social links"><span></span><span></span><span></span><span></span></div>
    <h4 class="footer-heading links-heading">QUICK LINKS</h4>
    <ul class="links">
      <li>Book Online</li>
      <li>Clients Login</li>
      <li>Contact</li>
    </ul>
    <h4 class="footer-heading news-heading">NEWSLETTER</h4>
    <div class="signup">
      <span class="signup-input">Your Email</span>
      <span class="signup-btn">Sign up</span>
    </div>
  </footer>
</div>
</body>
</html>
```